Brevanor Inc. Website

We need a website design for a new company based in Montreal, Canada. Our company offers professional services in planning & scheduling for major construction projects in varying industries. The main colors to be used are black & red (same as in logo). The final design should convey professionalism, precision, and excellence. The following are examples of what the website layout could look like: https://www.quilvardo.ca/, https://7496.ca/, https://lumavikt.ca/, https://www.dremorhext.com/en. Avoid using stock videos or photos with people in it.
Target audience are multi-national clients looking to hire a firm to manage their construction projects. Target market is Mining & Metals
Mining & Metalurgy, Hydroelectricity, Infrastructure
1 page

```html
<!DOCTYPE html>
<html lang="en">
<head>
<meta charset="utf-8">
<title>Brevanor Inc.</title>
<link rel="stylesheet" href="https://fonts.googleapis.com/css2?family=Fjalla+One&family=Montserrat:wght@400;500;600;700&display=swap">
<style>
:root{
  --red:#a3111c;
  --red-dark:#7d0c14;
  --ink:#111111;
  --text:#2a2a2a;
  --muted:#555;
  --white:#ffffff;
  --card-shadow:0 4px 18px rgba(0,0,0,.12);
  --footer:#1d1d1d;
  --footer-bar:#141414;
  --field:rgba(255,255,255,.28);
}
*{box-sizing:border-box;margin:0;padding:0}
html,body{width:1200px;height:3909px;overflow:hidden;background:var(--white)}
body{position:relative;font-family:"Montserrat",sans-serif;color:var(--text)}
.abs{position:absolute}
.heading{font-family:"Fjalla One",sans-serif;color:var(--ink);text-transform:uppercase;letter-spacing:.5px}
.btn{position:absolute;background:var(--red);color:var(--white);border-radius:6px;display:flex;align-items:center;justify-content:center;font-size:15px;font-weight:500}

/* hero */
.hero-bg{left:0;top:0;width:1200px;height:790px;background:linear-gradient(180deg,#e4ebf3 0%,#dbe3ec 15%,#9aa8b8 35%,#b7c0cb 55%,#d6dce3 75%,#ffffff 100%)}
.brand{font-family:"Montserrat",sans-serif;font-weight:700;font-size:24px;color:var(--red);display:flex;align-items:center;gap:10px}
.brand .dot{width:30px;height:30px;border-radius:50%;background:var(--red)}
.nav a{position:absolute;top:54px;font-size:15px;color:var(--ink);text-decoration:none}
.nav a.active{color:var(--red)}
.hero-title{left:0;width:1200px;top:272px;text-align:center;font-size:60px;line-height:64px}

/* about */
.about-card{left:111px;top:648px;width:978px;height:349px;background:var(--white);border-radius:20px;box-shadow:var(--card-shadow);overflow:hidden}
.about-photo{position:absolute;right:0;top:0;width:293px;height:349px;background:linear-gradient(160deg,#6f8aa6 0%,#3d5670 45%,#c58b4a 70%,#1f3046 100%);clip-path:polygon(30% 0,100% 0,100% 100%,45% 100%,0 50%)}
.about-card h2{position:absolute;left:45px;top:38px;font-size:32px}
.about-card p{position:absolute;left:45px;top:100px;width:628px;font-size:16px;line-height:29px;text-align:justify;color:#333}

/* section titles */
.section-title{left:0;width:1200px;text-align:center;font-size:34px}

.tile{position:absolute;border-radius:14px;overflow:hidden;box-shadow:var(--card-shadow)}
.tile .photo{position:absolute;inset:0}
.tile .label{position:absolute;left:24px;bottom:16px;font-family:"Fjalla One",sans-serif;color:var(--white);font-size:22px;line-height:23px;text-transform:uppercase}

/* articles */
.article{position:absolute;top:1625px;height:470px;background:var(--white);box-shadow:0 2px 10px rgba(0,0,0,.14)}
.article .photo{height:336px}
.article h3{position:absolute;top:360px;font-size:21px;font-weight:700;color:var(--ink)}
.article p{position:absolute;top:401px;font-size:15px;line-height:29px;color:#333}

/* projects */
.project{position:absolute;width:305px;height:242px;overflow:hidden}
.project .photo{position:absolute;inset:0}
.project .label{position:absolute;left:34px;top:180px;font-family:"Fjalla One",sans-serif;color:var(--white);font-size:22px;text-transform:uppercase}

/* contact */
.map-halo{left:114px;top:3000px;width:470px;height:470px;border-radius:50%;background:#f4dfe1}
.map{left:126px;top:3005px;width:460px;height:460px;border-radius:50%;background:radial-gradient(circle,#eef0ed 0%,#e6e9e4 70%,#d9ddd6 100%);box-shadow:0 0 0 6px rgba(255,255,255,.8)}
.location{left:114px;width:470px;top:3476px;text-align:center;font-weight:700;font-size:21px;letter-spacing:1px;color:var(--ink)}
.contact-panel{left:661px;top:2978px;width:539px;height:543px;border-radius:14px 0 0 14px;background:linear-gradient(180deg,#3a3937 0%,#4a4643 40%,#5a554f 70%,#3c3a38 100%)}
.contact-panel h2{position:absolute;left:0;width:100%;text-align:center;top:45px;color:var(--white);font-size:34px;padding-right:30px}
.field{position:absolute;left:75px;width:353px;background:var(--field);color:rgba(255,255,255,.75);font-size:15px;padding:0 18px;display:flex;align-items:center}

/* footer */
.footer{left:0;top:3585px;width:1200px;height:253px;background:var(--footer)}
.footer-bar{left:0;top:3838px;width:1200px;height:71px;background:var(--footer-bar);color:var(--white);font-size:13px;display:flex;align-items:center;justify-content:center}
.footer .col-title{position:absolute;top:68px;color:var(--white);font-weight:600;font-size:15px}
.footer .rule{position:absolute;top:91px;width:117px;height:2px;background:#bbb}
.footer ul{position:absolute;top:104px;list-style:none}
.footer li{color:var(--white);font-size:15px;line-height:26px}
.social{position:absolute;top:164px;width:30px;height:30px;border-radius:50%;background:var(--white)}
.newsletter{position:absolute;left:775px;top:106px;width:323px;height:44px;border-radius:6px;background:var(--white);border:1px solid var(--red);overflow:hidden}
.newsletter span{position:absolute;left:18px;top:12px;font-size:16px;color:#999}
.newsletter b{position:absolute;right:0;top:0;width:88px;height:100%;background:var(--red);color:var(--white);font-weight:500;font-size:16px;display:flex;align-items:center;justify-content:center}
</style>
</head>
<body>

<!-- Hero -->
<div class="abs hero-bg" role="img" aria-label="Wintry aerial view of the Montreal skyline"></div>
<div class="abs brand" style="left:114px;top:46px"><span class="dot"></span>Brevanor</div>
<nav class="nav">
  <a class="active" style="left:611px">Home</a>
  <a style="left:687px">About us</a>
  <a style="left:781px">Services</a>
  <a style="left:869px">Contact</a>
</nav>
<div class="btn" style="left:951px;top:42px;width:138px;height:41px">Enquire Now</div>
<h1 class="abs heading hero-title">Welcome to<br>Brevanor</h1>
<div class="btn" style="left:531px;top:420px;width:138px;height:40px">Get Started</div>

<!-- About -->
<section class="abs about-card">
  <div class="about-photo" role="img" aria-label="Cargo port with container cranes at dusk"></div>
  <h2 class="heading">About us</h2>
  <p>Lorem ipsum dolor sit amet, consectetur adipiscing elit, sed do eiusmod tempor incididunt ut labore et dolore magna aliqua. Quis ipsum suspendisse ultrices gravida. Risus commodo viverra maecenas accumsan lacus vel facilisis. Lorem ipsum dolor sit amet, consectetur adipiscing elit, sed do eiusmod tempor incididunt ut labore et dolore magna aliqua.</p>
  <div class="btn" style="left:42px;top:265px;width:138px;height:43px">Read More</div>
</section>

<!-- Services -->
<h2 class="abs heading section-title" style="top:1085px">Services</h2>
<div class="tile" style="left:285px;top:1186px;width:305px;height:241px">
  <div class="photo" role="img" aria-label="Planning meeting over construction drawings" style="background:linear-gradient(135deg,#cfcfcf,#8a8a8a 55%,#4a4a4a)"></div>
  <div class="label">Planning of<br>construction project</div>
</div>
<div class="tile" style="left:619px;top:1186px;width:305px;height:241px">
  <div class="photo" role="img" aria-label="Gantt schedule chart with a pen" style="background:linear-gradient(135deg,#d9dfe8,#8d9bb0 55%,#4f5d74)"></div>
  <div class="label">Scheduling of<br>construction project</div>
</div>

<!-- Articles -->
<h2 class="abs heading section-title" style="top:1533px">Articles</h2>
<article class="article" style="left:114px;width:487px">
  <div class="photo" role="img" aria-label="Construction site with engineers reviewing a tablet" style="background:linear-gradient(180deg,#a89a86,#7d7264 60%,#5d6b4a)"></div>
  <h3 style="left:30px">Articles 1</h3>
  <p style="left:28px;width:430px">Lorem ipsum dolor sit amet, consectetur adipiscing elit, sed do eiusmod tempor.</p>
</article>
<article class="article" style="left:614px;width:229px">
  <div class="photo" role="img" aria-label="Aerial view of high-rise towers under construction" style="background:linear-gradient(180deg,#8c9a8a,#6c7867 50%,#9a8f7d)"></div>
  <h3 style="left:24px">Articles 2</h3>
  <p style="left:24px;width:190px">Lorem ipsum dolor sit amet, consectetur.</p>
</article>
<article class="article" style="left:856px;width:230px">
  <div class="photo" role="img" aria-label="Engineer at an industrial plant with city towers behind" style="background:linear-gradient(180deg,#b9c6d2,#8a9fb0 50%,#6f8a6a)"></div>
  <h3 style="left:17px">Articles 3</h3>
  <p style="left:17px;width:200px">Lorem ipsum dolor sit amet, consectetur.</p>
</article>

<!-- Projects -->
<h2 class="abs heading section-title" style="top:2159px">Projects</h2>
<div class="project" style="left:114px;top:2262px"><div class="photo" role="img" aria-label="Open-pit mine" style="background:linear-gradient(160deg,#3c4046,#2a2d31 60%,#4a4d51)"></div><div class="label">Mining &amp; Metallurgy</div></div>
<div class="project" style="left:449px;top:2262px"><div class="photo" role="img" aria-label="Hydroelectric dam on a river" style="background:linear-gradient(160deg,#2e4a4e,#3d5a47 55%,#24373c)"></div><div class="label">Hydroelectricity</div></div>
<div class="project" style="left:783px;top:2262px"><div class="photo" role="img" aria-label="Highway interchange near a city" style="background:linear-gradient(160deg,#3f4a50,#3f5541 55%,#2e3b36)"></div><div class="label">Infrastructure</div></div>
<div class="project" style="left:114px;top:2533px"><div class="photo" role="img" aria-label="Heavy mining machinery on site" style="background:linear-gradient(160deg,#3a3d44,#5a4a33 55%,#2d2f33)"></div><div class="label">Industrial &amp; Mining</div></div>
<div class="project" style="left:449px;top:2533px"><div class="photo" role="img" aria-label="Nuclear power plant cooling towers" style="background:linear-gradient(160deg,#5a6256,#4a5245 55%,#353a33)"></div><div class="label">Nuclear</div></div>
<div class="btn" style="left:531px;top:2837px;width:138px;height:41px">View More</div>

<!-- Contact -->
<div class="abs map-halo"></div>
<div class="abs map" role="img" aria-label="Street map of Montreal with three location pins"></div>
<div class="abs location">MONTREAL, CANADA</div>
<section class="abs contact-panel" role="img" aria-label="Dusk view of an industrial waterfront behind the contact form">
  <h2 class="heading">Contact</h2>
  <div class="field" style="top:115px;height:46px">Name</div>
  <div class="field" style="top:179px;height:46px">Email</div>
  <div class="field" style="top:247px;height:46px">Phone</div>
  <div class="field" style="top:312px;height:96px;align-items:flex-start;padding-top:14px">Message</div>
  <div class="btn" style="left:178px;top:440px;width:155px;height:41px;font-size:17px">Submit</div>
</section>

<!-- Footer -->
<footer class="abs footer">
  <div class="abs brand" style="left:114px;top:60px;color:var(--white)"><span class="dot" style="background:var(--white)"></span>Brevanor</div>
  <span class="social" style="left:115px"></span>
  <span class="social" style="left:153px"></span>
  <span class="social" style="left:190px"></span>

  <div class="col-title" style="left:364px">Quick Links</div>
  <div class="rule" style="left:364px"></div>
  <ul style="left:364px"><li>Home</li><li>About Us</li><li>Services</li><li>Articles</li><li>Contact</li></ul>

  <div class="col-title" style="left:552px">Help Links</div>
  <div class="rule" style="left:552px"></div>
  <ul style="left:551px;line-height:24px"><li>Support</li><li>Terms &amp; Conditions</li><li>FAQ</li><li>Privacy Policy</li></ul>

  <div class="col-title" style="left:777px;top:66px">Subscribe Our Newsletter</div>
  <div class="newsletter"><span>Email</span><b>Submit</b></div>
</footer>
<div class="abs footer-bar">Copyright © 2023 Brevanor | All Rights Reserved</div>

</body>
</html>
```